Training Course Info Brochure

Hi there, I'm looking for a design for A4 Flyer (2-3 pages) on our new Course - Infection Control. I have included a previous brochure on our courses so the designed can see the look and feel we are looking for.

As this is about Infection Control, I would also like to see some RED in the design or wording.

The brochure will need to include quite a few industry/ government logos as well and graphics are important. I have included some (Health Care Industry workers) and am also open to other graphics.

Thanks for considering!

Target Market(s)

The Health profession and students wanting to work in the health field

Industry/Entity Type

Health Care

Font styles to use
Sans Serif

Colors
3277b5
f78f20
ffffff
ec1f27

Requirements
Must have
• Similar feel to the brochure I have included in this brief.

SOME RED lettering as we are teaching Infection Control during the COVID19 pandemic
Nice to have
• Lovely design with quite a few photos graphics

Company details:

Carrow Academy of Learning
RTO 73648
FREECALL : 1800 437 982
www.carrowlearning.edu.au
info@carrowlearning.edu.au

```html
<!DOCTYPE html>
<html lang="en">
<head>
<meta charset="utf-8">
<title>Infection Control Course – Carrow Academy of Learning</title>
<link href="https://fonts.googleapis.com/css2?family=Hind:wght@300;400;500;600&display=swap" rel="stylesheet">
<style>
  :root {
    --red: #ec1f27;
    --blue: #3277b5;
    --white: #ffffff;
    --text: #58595b;
    --photo-warm: #d9cfc4;
    --photo-cool: #c9d3dc;
    --glove: #7fb4e6;
  }
  * { margin: 0; padding: 0; box-sizing: border-box; }
  html, body { width: 848px; height: 1200px; overflow: hidden; background: var(--white); }
  body { font-family: "Hind", sans-serif; color: var(--text); font-weight: 300; position: relative; }
  .abs { position: absolute; }

  .format-banner { left: 0; top: 0; width: 430px; height: 80px; background: var(--red); color: var(--white); padding: 16px 0 0 19px; }
  .format-banner h1 { font-weight: 600; font-size: 29px; line-height: 1; }
  .format-banner p { font-weight: 400; font-size: 18px; line-height: 1; margin-top: 6px; }
  .format-banner small { font-size: 12px; }

  .photo { background: linear-gradient(135deg, var(--photo-warm), var(--photo-cool)); }
  .photo-study { left: 430px; top: 0; width: 418px; height: 269px; background: linear-gradient(135deg, #c8b8a2, #e8e2da 55%, #d2c7bc); }
  .photo-clinic { left: 0; top: 324px; width: 413px; height: 249px; background: linear-gradient(120deg, #f2f2f0, #b9c6d3 60%, #8fa6bd); }
  .photo-gloves { left: 430px; top: 808px; width: 418px; height: 183px; background: radial-gradient(ellipse at 50% 55%, var(--glove) 0%, #a9c8e4 35%, #d4d8de 70%); }

  .body-copy { font-size: 15.5px; line-height: 17px; }
  .body-copy p + p { margin-top: 8px; }
  .format-copy { left: 19px; top: 94px; width: 400px; }

  .section-title { color: var(--red); font-weight: 400; font-size: 19.5px; line-height: 20px; }
  .mentor { left: 430px; top: 318px; width: 405px; }
  .recognised { left: 430px; top: 456px; width: 405px; }
  .section-title + .body-copy { margin-top: 7px; }

  .skills-band { left: 0; top: 590px; width: 848px; height: 80px; background: var(--red); color: var(--white); padding: 28px 0 0 21px; }
  .skills-band h2 { font-weight: 600; font-size: 29px; line-height: 1; }

  .bullets { list-style: none; font-size: 15.5px; line-height: 17px; }
  .bullets li { position: relative; padding-left: 26px; margin-bottom: 8px; }
  .bullets li::before { content: ""; position: absolute; left: 2px; top: 7px; width: 4px; height: 4px; border-radius: 50%; background: #222; }
  .skills-left { left: 19px; top: 679px; width: 400px; }
  .skills-right { left: 434px; top: 678px; width: 400px; }

  .ideal { left: 19px; top: 876px; width: 400px; }
  .ideal .body-copy { margin-top: 12px; }
  .highlight { color: var(--blue); font-weight: 400; }
  .settings-title { left: 19px; top: 976px; width: 400px; font-size: 19.5px; line-height: 20px; }
  .settings-left { left: 17px; top: 1024px; width: 400px; }
  .settings-right { left: 430px; top: 1023px; width: 410px; }
</style>
</head>
<body>
  <header class="format-banner abs">
    <h1>Course format</h1>
    <p>Online with face-to-face tutorial <small>(in person or via Linkup)</small></p>
  </header>

  <div class="photo photo-study abs" role="img" aria-label="Smiling student studying at a desk with a laptop"></div>

  <section class="format-copy body-copy abs">
    <p>Our course is delivered to you online which allows you to undertaken study at your own pace. &nbsp; It is recommended completion occurs within a month.</p>
    <p>Once you have completed the Online Component of your course, &nbsp;you are invited into a Practical Lab Session via face to face learning; &nbsp;to practice skills and undertake a workplace simulated activity.</p>
    <p>Regional locations may be fulfilled by Linkup technology and Carrow may also conduct on-site visits as required. Carrow also travel to regional locations throughout the year. Group training sessions are also available for corporates and workplaces.</p>
  </section>

  <div class="photo photo-clinic abs" role="img" aria-label="Dental clinic worker holding a folder with a patient being treated behind"></div>

  <section class="mentor abs">
    <h3 class="section-title">Mentor Support and Practical Sessions</h3>
    <p class="body-copy">Students are welcomed to the course by a short induction by your Tutor/Mentor to start you on your way with confidence! &nbsp;All of Carrow’s student resources, learner materials, videos are contained in Carrow’s easy to use LMS and learning is provided online at your convenience.</p>
  </section>

  <section class="recognised abs">
    <h3 class="section-title">Industry Recognised</h3>
    <p class="body-copy">Carrow’s unique program in Infection Control is supported by leading Industry bodies, and includes certification by the Department of Health, and other leading Health bodies in Australia. Our Unit of competency is Australian Recognised and Accredited.</p>
  </section>

  <div class="skills-band abs"><h2>Gain these skills</h2></div>

  <ul class="bullets skills-left abs">
    <li>Gain Industry Certification in Hand Hygiene</li>
    <li>Gain Industry Certification in COVID19 Infection Control</li>
    <li>Gain Industry Certification in Cleaning, Disinfection and Sterilisation</li>
    <li>Using personal protective equipment safely (practical session with complimentary PPE samples)</li>
  </ul>
  <ul class="bullets skills-right abs">
    <li>Understanding the chain of infection</li>
    <li>Identify infection hazards and assess risks</li>
    <li>How to prevent the spread and transmission of infection</li>
    <li>Maintaining a clean work environment</li>
  </ul>

  <div class="photo photo-gloves abs" role="img" aria-label="Hands in blue medical gloves forming a heart shape"></div>

  <section class="ideal abs">
    <h3 class="section-title">Who this course is ideal for</h3>
    <p class="body-copy">The skill set course is most suitable <span class="highlight">for anyone working the healthcare sector, or those looking to enter employment in the health fields.</span></p>
  </section>

  <h3 class="section-title settings-title abs">This training is for care workers across all health care settings, including</h3>

  <ul class="bullets settings-left abs">
    <li>Hospitals</li>
    <li>Primary care</li>
    <li>Aged care (both in residential aged care facilities or with visiting carers at home, including cleaners and cooks)</li>
    <li>Dental practices, including dentists, nurses, cleaners and receptionists</li>
  </ul>
  <ul class="bullets settings-right abs">
    <li>Disability (both in residential/shared care facilities or part-time carers in people’s homes, including cleaners and cooks)</li>
    <li>Allied health</li>
    <li>Aboriginal Community Controlled Health Services</li>
    <li>Pharmacies</li>
    <li>Medical practices, allied health, GP and specialist clinics</li>
  </ul>
</body>
</html>
```